Redesign of Brightvale.com website

Our website was initially developed 6+ years ago and has been maintained by several different designers. As a result, it is overly complex, inconsistent format/layout and the content is not well structured/easy to navigate

We need the site redeveloped with a more modern look and feel, simpler content structure and ability to implement new/improved tools, such as: Dynamic Forms, Sales Funnels, Landing Pages, improved metadata of our pages and posts, improved SEO/Page ranking, etc.

We currently use SalesForce CRM, Constant Contact for marketing automation and SmartSheet forms. We are investigating Zapier for workflow integration which could extend to our website.

Our current website is developed in WordPress, ideally we will stick with this platform, but we’re happy to consider other CMS' if strongly recommended. We may decide to remove/consolidate some of the pages and/or content as part of this re-design.

We don't want to rebrand (ie change corporate logo, colours scheme etc) as part of this website redevelopment and it is critical that we don't lose our current Page Ranking, SEO rankings, backlink benefits, etc as part of this redevelopment.

Sites we like the feel/design of are: plorvista.com, quindlefax.com and tovalip.com

Target Market(s)

Corporate, Enterprise and Government B2B clients.

Coding

Coded - Design and coding required

Number of Pages Required

5+ page

Font styles to use
Sans Serif

Colors
ffffff
ec1f27

Requirements
Must have
• Must retain the majority of content on our existing website (although we may re-write some of it as part of this redesign process).
Nice to have
• See above "Project Description"
Should not have

```html
<!DOCTYPE html>
<html lang="en">
<head>
<meta charset="utf-8">
<title>Brightvale – Business Continuity Advisors</title>
<link rel="stylesheet" href="https://fonts.googleapis.com/css2?family=Poppins:wght@300;400;500;600;700&display=swap">
<style>
:root{
  --red:#e8262b;
  --red-dark:#c81a20;
  --ink:#222326;
  --text:#6b6b6b;
  --muted:#9a9a9a;
  --cream:#fffbf3;
  --panel:#e9e9e9;
  --soft:#f6f6f6;
  --strip:#ececec;
  --white:#ffffff;
  --band:#4b4b4d;
}
*{box-sizing:border-box;margin:0;padding:0}
html,body{width:1200px;height:5263px;overflow:hidden}
body{font-family:"Poppins",sans-serif;color:var(--ink);background:var(--white);position:relative}
section,header,footer{position:relative;width:1200px;overflow:hidden}
.abs{position:absolute}
.eyebrow{color:var(--red);font-size:15px;font-weight:400}
.title{font-size:31px;font-weight:500;color:var(--ink);line-height:1.25}
.body{font-size:14px;line-height:22.5px;color:var(--text)}
.btn{position:absolute;display:flex;align-items:center;justify-content:center;background:var(--red);color:#fff;font-size:11px;font-weight:600;border-radius:24px;box-shadow:0 8px 18px rgba(232,38,43,.28);text-decoration:none}
.center{left:0;width:1200px;text-align:center}
.art{position:absolute;border-radius:12px}

/* header / hero */
.hero{height:568px;background:var(--cream)}
.brand{position:absolute;display:flex;align-items:center;gap:8px}
.brand-dot{width:22px;height:22px;border-radius:50%;background:var(--red)}
.brand-name{font-size:19px;font-weight:400;color:var(--red);line-height:1}
.brand-tag{font-size:6px;color:var(--muted);margin-top:2px}
.nav{position:absolute;left:460px;top:31px;display:flex;gap:24px;font-size:12px;color:#333}
.login{position:absolute;left:934px;top:22px;width:82px;height:36px;border:1.5px solid #888;border-radius:20px;display:flex;align-items:center;justify-content:center;font-size:12px;color:#333}
.hero h1{position:absolute;left:184px;top:178px;font-size:41px;line-height:50px;font-weight:500}
.hero h1 strong{font-weight:600}

/* about */
.about{height:650px}

/* services */
.services{height:618px}
.svc-panel{position:absolute;left:0;top:0;width:640px;height:618px;background:var(--panel)}
.svc-item{position:absolute;left:249px;width:391px;height:74px;display:flex;align-items:center;padding-left:52px;gap:22px;font-size:16px;font-weight:500;color:var(--ink)}
.svc-item.active{background:var(--white);border-left:3px solid var(--red);padding-left:49px}
.svc-icon{width:28px;height:28px;display:flex;align-items:center;justify-content:center}
.svc-icon.boxed{background:#ececec;border-radius:6px}
.svc-list{position:absolute;left:683px;top:132px;width:340px;list-style:none}
.svc-list li{position:relative;padding-left:32px;font-size:13.5px;color:#333;line-height:22px;margin-bottom:15px}
.svc-list li::before{content:"";position:absolute;left:4px;top:7px;width:8px;height:8px;border:1.5px solid var(--red);transform:rotate(45deg)}

/* strategy */
.strategy{height:562px}

/* team */
.team{height:772px;background:var(--soft)}
.card{position:absolute;top:210px;width:260px;height:370px;background:var(--white)}
.card-photo{height:276px;background:linear-gradient(180deg,#e4e4e4,#cfcfcf)}
.card-name{text-align:center;font-size:15px;font-weight:500;margin-top:24px}
.card-role{text-align:center;font-size:11px;color:var(--muted);margin-top:6px}

/* testimonials */
.testimonials{height:510px}
.client-mark{position:absolute;left:323px;top:229px;width:172px;height:172px;border-radius:50%;background:linear-gradient(145deg,#ffa23a,#ff3e6a 60%,#ff2ea0);display:flex;align-items:center;justify-content:center;color:#fff;font-size:22px;font-weight:600;box-shadow:0 16px 36px rgba(255,70,110,.3)}
.quote{position:absolute;left:540px;top:264px;width:340px;font-size:14px;line-height:22.5px;color:#444}
.stars{position:absolute;left:540px;top:218px;color:#f5a623;font-size:15px;letter-spacing:1px}

.logo-strip{height:156px;background:var(--strip)}
.logo-strip::before{content:"";position:absolute;left:591px;top:0;border-left:10px solid transparent;border-right:10px solid transparent;border-top:10px solid var(--white)}
.chip{position:absolute;top:38px;width:78px;height:78px;border-radius:50%;background:var(--white);display:flex;align-items:center;justify-content:center;font-size:11.5px;font-weight:500;color:#555;box-shadow:0 6px 14px rgba(0,0,0,.06)}
.chip.active{background:linear-gradient(145deg,#ff8a2a,#ff2e8a);color:#fff}
.arrow{position:absolute;top:68px}

/* blog */
.blog{height:820px}
.tabs{position:absolute;top:201px;left:0;width:1200px;display:flex;justify-content:center;gap:22px;font-size:13px;color:#b5b5b5}
.tabs .on{color:var(--red)}
.post{position:absolute;top:256px;width:262px}
.post-img{height:200px;background:linear-gradient(160deg,#d9d6d0,#9e968c)}
.post-date{font-size:11px;color:var(--muted);margin-top:30px}
.post-title{font-size:16.5px;font-weight:600;line-height:23px;margin-top:10px}
.post-text{font-size:13px;line-height:21.5px;color:var(--text);margin-top:10px}

/* contact band */
.cta{height:262px;background:linear-gradient(100deg,#3e3e40,#5a5a5c)}
.cta-btn{position:absolute;left:838px;top:121px;width:178px;height:59px;background:var(--white);border-radius:30px;display:flex;align-items:center;justify-content:center;color:var(--red);font-size:14px;font-weight:600}

/* footer */
.footer{height:345px;background:#f3f3f3}
.f-head{position:absolute;top:72px;font-size:14px;font-weight:500}
.f-links{position:absolute;top:121px;list-style:none;font-size:12px;color:#444}
.f-links li{height:30px}
.f-contact{position:absolute;left:803px;top:121px;font-size:12px;color:#444;line-height:17px}
.f-contact .row{position:relative;padding-left:36px;margin-bottom:14px}
.f-contact svg{position:absolute;left:0;top:2px}
.social{position:absolute;left:184px;top:214px;display:flex;gap:12px}
.social span{width:9px;height:9px;border-radius:50%;background:#333}
.copy{position:absolute;top:304px;font-size:10px;color:#666}
</style>
</head>
<body>

<!-- HERO -->
<header class="hero">
  <div class="brand" style="left:184px;top:24px">
    <div class="brand-dot"></div>
    <div><div class="brand-name">brightvale</div><div class="brand-tag">trusted advisor</div></div>
  </div>
  <nav class="nav"><span>Home</span><span>Service</span><span>About</span><span>Clients</span><span>Resources</span><span>Blog</span><span>Contact</span></nav>
  <div class="login">login</div>

  <p class="eyebrow abs" style="left:184px;top:138px">Welcome TO</p>
  <h1>We Provide<br><strong>Business Solution</strong></h1>
  <p class="body abs" style="left:184px;top:298px;width:330px">Lorem ipsum dolor sit amet consectetur adipisicing elit seddo eiusm.</p>
  <a class="btn" style="left:184px;top:378px;width:139px;height:45px">Our Services</a>

  <div class="art" role="img" aria-label="Illustration of a woman holding a report beside floating analytics charts and a potted plant" style="left:603px;top:92px;width:400px;height:398px;background:linear-gradient(160deg,#fbf3ea,#f3e3d6)"></div>
</header>

<!-- ABOUT -->
<section class="about">
  <div class="art" role="img" aria-label="Illustration of a woman at a desk with a laptop, desk lamp and floating charts" style="left:188px;top:96px;width:435px;height:460px;background:linear-gradient(160deg,#f4f4f4,#e9e4e4)"></div>
  <p class="eyebrow abs" style="left:683px;top:106px">Our Short Story</p>
  <h2 class="title abs" style="left:683px;top:150px">About Our Agency</h2>
  <p class="body abs" style="left:683px;top:212px;width:320px">Brightvale Is Your Trusted Advisor For Business Continuity Solutions Brightvale's business continuity consultant's providing two core services: Business Continuity Managed services Business Continuity Consulting services Managed Continuity Service Do your business continuity and disaster recovery plans quickly become out of date?</p>
  <a class="btn" style="left:683px;top:468px;width:140px;height:47px">More About us</a>
</section>

<!-- SERVICES -->
<section class="services">
  <div class="svc-panel">
    <p class="eyebrow abs" style="left:289px;top:63px">What we do</p>
    <h2 class="title abs" style="left:289px;top:103px">Our Best Services</h2>
  </div>
  <div class="svc-item" style="top:182px"><span class="svc-icon"><svg width="24" height="20" viewBox="0 0 24 20" fill="none" stroke="#333" stroke-width="1.5"><path d="M2 8l5-4 5 3 5-3 5 4-5 6-5-4-5 4z"/></svg></span>Resilience &amp; Continuity</div>
  <div class="svc-item" style="top:260px"><span class="svc-icon"><svg width="22" height="22" viewBox="0 0 22 22" fill="none" stroke="#333" stroke-width="1.5"><circle cx="11" cy="11" r="8"/><path d="M11 6v5l3 3"/></svg></span>Security Management</div>
  <div class="svc-item active" style="top:339px"><span class="svc-icon boxed" style="width:38px;height:38px"><svg width="20" height="20" viewBox="0 0 20 20" fill="none" stroke="#333" stroke-width="1.5"><circle cx="12" cy="8" r="5"/><path d="M8 12l-5 5"/></svg></span>IT Services &amp; Solutions</div>
  <div class="svc-item" style="top:413px"><span class="svc-icon"><svg width="22" height="22" viewBox="0 0 22 22" fill="none" stroke="#333" stroke-width="1.5"><path d="M4 14a7 7 0 1 1 12 0v4H4z"/><circle cx="11" cy="10" r="2"/></svg></span>Data Management</div>
  <div class="svc-item" style="top:493px"><span class="svc-icon"><svg width="22" height="22" viewBox="0 0 22 22" fill="none" stroke="#333" stroke-width="1.5"><circle cx="11" cy="11" r="4"/><path d="M11 2v3M11 17v3M2 11h3M17 11h3M5 5l2 2M15 15l2 2M5 17l2-2M15 7l2-2"/></svg></span>Software Solutions</div>

  <h2 class="abs" style="left:683px;top:64px;font-size:20px;font-weight:500">IT Services &amp; Solutions</h2>
  <ul class="svc-list">
    <li>ResPlan Recovery Planner (BCM Software)</li>
    <li>Relay Mobile Incident Response Application</li>
    <li>Solution Design &amp; Implementation</li>
    <li>IT Service Management (ITIL/ITSM)</li>
    <li>IT Process &amp; Policy Development</li>
    <li>IT Sourcing Strategy</li>
    <li>CivicDC Migration Strategy</li>
    <li>Technology Refresh Strategy</li>
    <li>ITIL Audits</li>
    <li>Cloud Risk Assessment</li>
    <li>Technical User Training</li>
  </ul>
  <a class="btn" style="left:683px;top:570px;width:140px;height:48px">Learn More</a>
</section>

<!-- STRATEGY -->
<section class="strategy">
  <p class="eyebrow abs" style="left:184px;top:92px">Our Strategy</p>
  <h2 class="title abs" style="left:184px;top:134px;font-size:31px;font-weight:600;line-height:40px">How To Ensure Your<br>Business Is 100% Safe</h2>
  <p class="body abs" style="left:184px;top:236px;width:300px">Your business is only as strong as its weakest link. As an executive in any business, it is understandable that you want to ensure it is 100% safe, because your business is only as strong as its weakest link.</p>
  <a class="btn" style="left:184px;top:396px;width:141px;height:45px">More About us</a>
  <div class="art" role="img" aria-label="Illustration of two colleagues presenting growth charts on a large board" style="left:527px;top:96px;width:505px;height:374px;background:linear-gradient(160deg,#f6f6f6,#ebe6e6)"></div>
</section>

<!-- TEAM -->
<section class="team">
  <p class="eyebrow abs center" style="top:93px">Our Team</p>
  <h2 class="title abs center" style="top:130px">Meet The Team</h2>
  <div class="card" style="left:184px"><div class="card-photo" role="img" aria-label="Portrait photo of a smiling bearded man with arms crossed"></div><div class="card-name">Liam Ostrander</div><div class="card-role">Managing Director</div></div>
  <div class="card" style="left:468px"><div class="card-photo" role="img" aria-label="Portrait photo of a smiling man in a denim shirt with arms crossed"></div><div class="card-name">Marco Pellini</div><div class="card-role">Principal Consultant</div></div>
  <div class="card" style="left:754px"><div class="card-photo" role="img" aria-label="Portrait photo of a smiling woman in a black blazer with arms crossed"></div><div class="card-name">Greta Holloway</div><div class="card-role">Senior Consultant</div></div>
  <a class="btn" style="left:531px;top:631px;width:139px;height:49px">View More</a>
</section>

<!-- TESTIMONIALS -->
<section class="testimonials">
  <p class="eyebrow abs center" style="top:92px">Testimonials</p>
  <h2 class="title abs center" style="top:134px">What Our Clients Say</h2>
  <div class="client-mark">Corvana</div>
  <div class="stars">★★★★☆</div>
  <p class="quote">“With all due respect, I don't see Brightvale in the classic consultant mould. I see you far more as 'hands-on implementation practitioners', working closely with us to define and implement real solutions to meet our business strategies”</p>
  <p class="abs" style="left:540px;top:413px;font-size:14px;font-weight:500">Daniel Reeve, Head of Delivery Management</p>
  <p class="abs" style="left:540px;top:445px;font-size:13px;color:var(--text)">Infrastructure Services, Corvana</p>
</section>

<section class="logo-strip">
  <svg class="arrow" style="left:299px" width="12" height="20" viewBox="0 0 12 20" fill="none" stroke="#333" stroke-width="1.6"><path d="M10 2L2 10l8 8"/></svg>
  <div class="chip" style="left:358px">Justora</div>
  <div class="chip" style="left:460px">Fenwick</div>
  <div class="chip active" style="left:562px">Corvana</div>
  <div class="chip" style="left:666px">Halcourt</div>
  <div class="chip" style="left:770px">Unitara</div>
  <svg class="arrow" style="left:893px" width="12" height="20" viewBox="0 0 12 20" fill="none" stroke="#333" stroke-width="1.6"><path d="M2 2l8 8-8 8"/></svg>
</section>

<!-- BLOG -->
<section class="blog">
  <p class="eyebrow abs center" style="top:90px">Our Blogs</p>
  <h2 class="title abs center" style="top:128px">The Latest News</h2>
  <div class="tabs"><span class="on">View All</span><span>Busniness Continuity</span><span>Disaster Recovery</span><span>Pandemic</span></div>
  <article class="post" style="left:184px"><div class="post-img" role="img" aria-label="Photo of a laptop, glasses and notebook on white linen" style="background:linear-gradient(160deg,#f2f0ee,#c9c5c0)"></div><p class="post-date">Date - 23/02/2021</p><h3 class="post-title">Decommissioning is Part of Disaster Recovery Planning.</h3><p class="post-text">More moving parts mean more chance of failure. Replace “moving parts” by “comatose IT servers”.</p></article>
  <article class="post" style="left:468px"><div class="post-img" role="img" aria-label="Photo of team members stacking hands over a desk" style="background:linear-gradient(160deg,#8c6a52,#3f3a3a)"></div><p class="post-date">Date - 24/02/2021</p><h3 class="post-title">Adapt or Die – A Darwinian Take on Business Continuity</h3><p class="post-text">Most businesses experience change constantly. Markets, technologies, regulations.</p></article>
  <article class="post" style="left:754px"><div class="post-img" role="img" aria-label="Photo of people working with a laptop and papers on a wooden desk" style="background:linear-gradient(160deg,#c8b9a4,#7d6a58)"></div><p class="post-date">Date - 25/02/2021</p><h3 class="post-title">How's Your User Experience for Your Disaster Recovery?</h3><p class="post-text">It may sound strange to talk about “touchy-feely” stuff like user experience in the.</p></article>
  <a class="btn" style="left:531px;top:679px;width:139px;height:49px">View More</a>
</section>

<!-- CONTACT BAND -->
<section class="cta" role="img" aria-label="Dark office photo background" style="">
  <p class="abs" style="left:182px;top:72px;color:#fff;font-size:15px">Contact us</p>
  <h2 class="abs" style="left:182px;top:108px;color:#fff;font-size:29px;font-weight:600;line-height:38px;font-style:italic">Any Questions? Contact us Freely<br>and We'll Get Back to You .</h2>
  <div class="cta-btn">Contact Now!</div>
</section>

<!-- FOOTER -->
<footer class="footer">
  <div class="brand" style="left:184px;top:78px">
    <div class="brand-dot"></div>
    <div><div class="brand-name">brightvale</div><div class="brand-tag">trusted advisor</div></div>
  </div>
  <p class="abs" style="left:184px;top:136px;width:210px;font-size:11px;line-height:15.5px;color:#444">Lorem ipsum dolor sit amet, con sectetur adipisicing elit, sed do eiusmod tempor.</p>
  <div class="social"><span></span><span></span><span></span><span></span></div>

  <h4 class="f-head" style="left:507px">Quick Links</h4>
  <ul class="f-links" style="left:507px"><li>Home</li><li>About us</li><li>Service</li><li>Blogs</li></ul>
  <h4 class="f-head" style="left:664px">Help</h4>
  <ul class="f-links" style="left:664px"><li>Team</li><li>Contact us</li><li>Login</li><li>Privacy policy</li></ul>
  <h4 class="f-head" style="left:803px">Contact Us</h4>
  <div class="f-contact">
    <div class="row"><svg width="12" height="14" viewBox="0 0 12 14" fill="none" stroke="#333" stroke-width="1.2"><path d="M6 13s5-5 5-8A5 5 0 0 0 1 5c0 3 5 8 5 8z"/><circle cx="6" cy="5" r="1.8"/></svg>Level 14, Tower 3 Harbour Quay,<br>88 Keel Street,<br>Sydney NSW 2000 Australia</div>
    <div class="row"><svg width="12" height="12" viewBox="0 0 12 12" fill="none" stroke="#333" stroke-width="1.2"><path d="M2 1h3l1 3-2 1a7 7 0 0 0 3 3l1-2 3 1v3c-6 0-10-4-10-9z"/></svg>1300 BV PLAN</div>
    <div class="row"><svg width="13" height="10" viewBox="0 0 13 10" fill="none" stroke="#333" stroke-width="1.2"><rect x="0.6" y="0.6" width="11.8" height="8.8"/><path d="M1 1l5.5 4.5L12 1"/></svg>info@brightvale.com</div>
  </div>
  <p class="copy center">Copyright © 2021 All rights reserved</p>
</footer>

</body>
</html>
```